Functional Beverage Bottle Labele

I need a label created for a functional beverage. A functional beverage is a drink that provides a function as well as being a beverage. This drink aims to help ease stress and allow women to relax at the end of their day. It has been designed specifically with women in mind (men can also drink it though).

The brand values are:
Natural - we use nature to nurture our best selves, Nourishing - in the ingredients we use and messages we share, Nimble - in the way we respond to our customers and operate on a daily basis

I am looking for a modern, clean looking label. The label will be going on to a clear 330ml flint ROPP bottle, with a silver ROPP cap and contains a light pink liquid. I have attached a mock up for you to see the colour of the liquid and the style of the bottle.

I have included further information in the design brief, colour palette, logo and other items to assist you with the process of designing the label. Happy to answer any questions. I am based in Melbourne Australia.

I have uploaded the files individually and as a zip file.

Target Market(s)

Australian females aged from 21 - 60

Font styles to use
Serif
Sans Serif
Decorative
Script

Requirements
Must have
• Required on the front of the label:

Brand Logo - attached

Drink function - the function of this drink is RELAX. There will be two others in the product line, REVIVE and RECOVER. Please include RELAX somewhere on the front.

Drink flavour
Native Strawberry Gum

Drink measurement
330mL

Product description
Sparkling water with adaptogens to help you adapt to life stressors

Key call outs - 100% natural, Sugar free

There are other requirements for the remainder of the label that I have included in the document attached.
Nice to have
• Please feel free to add icons, lines, etc to make the design the best it can be and give it some personality.

The map of Victoria that I have asked to be included should not be on the front and it should be no bigger than the barcode.
Should not have
• UPDATED: There should be no strawberry images on the bottle. The Native Strawberry Gum flavour comes from the leaves of a type of eucalyptus tree grown in Australia. I have added a photo of the leaves.

```html
<!DOCTYPE html>
<html lang="en">
<head>
<meta charset="utf-8">
<title>Attune Drinks – Relax label</title>
<link rel="stylesheet" href="https://fonts.googleapis.com/css2?family=Montserrat:wght@200;300;400;600;700&family=Roboto+Condensed:wght@400;700&display=swap">
<style>
  :root {
    --backdrop: #ebb2c4;
    --label-pink: #f8dde8;
    --band-pink: #ebb1c3;
    --sky-blue: #a8c5e8;
    --ink-blue: #5564a8;
    --relax-pink: #e7a2b8;
    --white: #ffffff;
    --table-ink: #2b2b3a;
  }
  * { box-sizing: border-box; margin: 0; padding: 0; }
  html, body { width: 1200px; height: 826px; overflow: hidden; }
  body {
    background: var(--backdrop);
    font-family: "Montserrat", sans-serif;
    position: relative;
  }
  .label {
    position: absolute;
    left: 40px; top: 141px;
    width: 1120px; height: 543px;
    background: var(--label-pink);
    overflow: hidden;
    color: var(--ink-blue);
  }
  .abs { position: absolute; }

  .brand-story {
    left: 28px; top: 32px; width: 280px;
    text-align: center;
    font-size: 11.6px; line-height: 21.6px; font-weight: 400;
  }
  .founder-signature {
    left: 97px; top: 234px; width: 137px; height: 40px;
    background: linear-gradient(90deg, rgba(85,100,168,.35), rgba(85,100,168,.15));
    border-radius: 20px;
  }
  .company-details {
    left: 337px; top: 36px; width: 200px;
    text-align: right; font-size: 11px; line-height: 12.5px;
    color: var(--table-ink); font-style: normal;
  }
  .company-details .company-name { font-weight: 700; }
  .company-details .web { margin-top: 18px; }
  .company-details .web strong { font-weight: 700; }
  .social-handle {
    left: 416px; top: 144px; font-size: 11px;
    display: flex; align-items: center; gap: 6px;
    color: var(--table-ink);
  }
  .social-handle .dot { width: 11px; height: 11px; border-radius: 50%; background: var(--relax-pink); }
  .origin-map {
    left: 416px; top: 179px; width: 119px; height: 92px;
    background: var(--ink-blue); border-radius: 12px 30px 40px 8px;
  }
  .origin-caption { left: 406px; top: 276px; width: 120px; text-align: center; font-size: 9.5px; color: var(--table-ink); }

  .function-name {
    left: 700px; top: 46px; width: 296px; text-align: center;
    font-size: 28px; font-weight: 300; letter-spacing: 30px; padding-left: 30px;
    color: var(--relax-pink);
  }
  .brand-name {
    left: 640px; top: 130px; width: 416px; text-align: center;
    font-size: 76px; font-weight: 200; letter-spacing: 4px; line-height: 90px;
  }
  .brand-sub {
    left: 640px; top: 222px; width: 416px; text-align: center;
    font-size: 22px; font-weight: 400; letter-spacing: 6px;
  }

  .flavour-band {
    left: 0; top: 313px; width: 100%; height: 30px;
    background: var(--band-pink);
  }
  .serving-tip {
    left: 20px; top: 320px; width: 540px; text-align: center;
    font-size: 13px; letter-spacing: 1.8px; color: var(--white); font-weight: 300;
  }
  .flavour-name {
    left: 600px; top: 315px; width: 500px; text-align: center;
    font-size: 20px; letter-spacing: 4px; color: var(--white); font-weight: 300;
  }
  .lower-panel {
    left: 0; top: 343px; width: 100%; height: 200px;
    background: linear-gradient(180deg, var(--label-pink) 0%, #d6cde6 45%, var(--sky-blue) 100%);
  }

  .nutrition-panel {
    left: 23px; top: 350px; width: 232px;
    border: 1px solid var(--table-ink);
    font-family: "Roboto Condensed", sans-serif; font-size: 10.5px; color: var(--table-ink);
    background: rgba(255,255,255,.12);
  }
  .nutrition-panel h3 { font-size: 13px; font-weight: 700; text-align: center; border-bottom: 1px solid var(--table-ink); padding: 2px 0; }
  .nutrition-panel .servings { font-weight: 700; padding: 2px 8px; border-bottom: 1px solid var(--table-ink); }
  .nutrition-panel table { width: 100%; border-collapse: collapse; }
  .nutrition-panel th { font-weight: 700; text-align: right; line-height: 11px; padding: 3px 8px 4px 0; border-bottom: 1px solid var(--table-ink); }
  .nutrition-panel td { text-align: right; padding: 0 8px 0 0; line-height: 14.5px; }
  .nutrition-panel td:first-child { text-align: left; padding-left: 8px; }
  .nutrition-panel tr:nth-child(2) td { padding-top: 4px; }

  .ingredients {
    left: 264px; top: 349px; width: 146px; font-size: 9px; line-height: 11.6px; color: var(--table-ink);
  }
  .ingredients strong { font-weight: 700; }
  .refund-mark { left: 264px; top: 474px; font-size: 13px; font-weight: 700; color: var(--ink-blue); display: flex; align-items: center; gap: 3px; }
  .refund-note { left: 264px; top: 497px; width: 150px; font-size: 9.5px; line-height: 11px; color: var(--table-ink); }

  .product-description {
    left: 648px; top: 378px; width: 400px; text-align: center;
    font-size: 14px; line-height: 22px; color: var(--white); font-weight: 400;
  }
  .callouts { left: 698px; top: 463px; width: 300px; display: flex; justify-content: center; align-items: center; color: var(--white); font-size: 11px; line-height: 14px; text-align: center; }
  .callouts span { width: 90px; }
  .callouts .divider { width: 1px; height: 34px; background: var(--ink-blue); margin: 0 15px; opacity: .6; }
  .volume { left: 792px; top: 514px; width: 100px; text-align: center; font-size: 9px; font-weight: 600; color: var(--white); }
</style>
</head>
<body>
  <main class="label">
    <p class="abs brand-story">Attune Drinks is a female-founded, female-focused, and female inspired beverage company created by me - Maren Ellis! Attune Drinks intimately understands the stressors on modern women and the impact this has on their well being. My mission is to make amazing drinks from adaptogenic herbs to help women adapt to stress, feel better, perform better, and live life with calm energy.</p>
    <div class="abs founder-signature" role="img" aria-label="Handwritten signature of the founder, Maren Ellis"></div>

    <address class="abs company-details">
      <div class="company-name">ATTUNE DRINKS</div>
      <div>Suite 210</div>
      <div>48 Harbour Lane</div>
      <div>Kestrel Vic 3991</div>
      <div class="web">Learn more at<br><strong>attunedrinks.com.au</strong></div>
    </address>
    <div class="abs social-handle"><span class="dot"></span>@attunedrinks</div>
    <div class="abs origin-map" role="img" aria-label="Map of the home state with the bottling town marked"></div>
    <div class="abs origin-caption">Bottled in Wrenfield</div>

    <div class="abs function-name">RELAX</div>
    <div class="abs brand-name">ATTUNE</div>
    <div class="abs brand-sub">drinks</div>

    <div class="abs flavour-band"></div>
    <div class="abs serving-tip">Best served chilled. Enjoy one bottle in the afternoon</div>
    <div class="abs flavour-name">NATIVE STRAWBERRY GUM</div>
    <div class="abs lower-panel"></div>

    <section class="abs nutrition-panel">
      <h3>NUTRITIONAL INFORMATION</h3>
      <div class="servings">Servings per package: 1 Serving size: 330mL</div>
      <table>
        <tr><th></th><th>Average<br>Per Serve</th><th>Average<br>Per 100mL</th></tr>
        <tr><td>Energy</td><td>(3 cal) 13 kJ</td><td>(1 cal) 4 kJ</td></tr>
        <tr><td>Protein</td><td>Less than 0.3g</td><td>Less than 0.1g</td></tr>
        <tr><td>Fat Total</td><td>Less than 0.3g</td><td>Less than 0.1g</td></tr>
        <tr><td>&nbsp;- Saturated</td><td>Less than 0.3g</td><td>Less than 0.1g</td></tr>
        <tr><td>Carbohydrate</td><td>0.7g</td><td>0.2g</td></tr>
        <tr><td>&nbsp;- Sugars</td><td>0g</td><td>0g</td></tr>
        <tr><td>Sodium</td><td>2.1mg</td><td>0.7mg</td></tr>
      </table>
    </section>

    <p class="abs ingredients"><strong>Ingredients:</strong> Carbonated water, Monk Fruit Juice (from Concentrate), Strawberry Gum Extract, L-Theanine, Schisandra Berry Extract, Panax Ginseng Extract, Rosemary Extract, Red Radish Juice Extract, Purple Carrot Juice Extract</p>
    <div class="abs refund-mark">
      <svg width="16" height="16" viewBox="0 0 16 16" aria-hidden="true"><circle cx="8" cy="8" r="6" fill="none" stroke="currentColor" stroke-width="2"/><path d="M8 1 L12 3 L8 5 Z" fill="currentColor"/></svg>10
    </div>
    <p class="abs refund-note">10c refund at collection depots/points in participating State/Territory of purchase</p>

    <p class="abs product-description">Sparkling water with adaptogens<br>to help you adapt to life stressors</p>
    <div class="abs callouts"><span>100%<br>NATURAL</span><span class="divider"></span><span>SUGAR<br>FREE</span></div>
    <div class="abs volume">330mL</div>
  </main>
</body>
</html>
```